Zielgruppe
Beamer Vermietung
Aufgabenstellung
Erstellung 2 professionell aussehender Webseiten.
Projektor-Verleih-Region-Wendlar.de
sowie
Projektor-Verleih-Region-Haselfurtheim.de
Die Seiten sind aktuell im Betrieb, aber haben ein sehr veraltetes Design.
Die Seiten können ähnlich aussehen, sollten aber etwas unterschiedlich sein, damit sie für den Kunden leicht anders aussehen.
Wichtig ist, dass alle Seiten, inklusive Startseite, Unterseiten und Links designed werden und das dieses Design in die bestehende Wordpress Installation eingepflegt wird.
Es ist also notwendig, gute Wordpress Kenntnisse zu haben um dann auch zwei fertige Wordpress Seiten liefern zu können.

```html
<!DOCTYPE html>
<html lang="de">
<head>
<meta charset="utf-8">
<title>Reservieren – Projektor Verleih</title>
<link href="https://fonts.googleapis.com/css2?family=Roboto:wght@300;400;500;700&family=Roboto+Condensed:wght@400&display=swap" rel="stylesheet">
<style>
:root{
  --green:#97c24b;
  --navy:#2c3c57;
  --navy-2:#34476a;
  --grey-bar:#ebebeb;
  --grey-soft:#eeeeee;
  --text-muted:#7a7a7a;
  --white:#ffffff;
}
*{margin:0;padding:0;box-sizing:border-box}
html,body{width:1200px;height:1168px;overflow:hidden;background:var(--white)}
body{position:relative;font-family:"Roboto",Arial,sans-serif;color:var(--navy)}
.abs{position:absolute}

.topbar{left:0;top:0;width:1200px;height:31px;background:var(--grey-bar);border-bottom:1px solid #d8d8d8}
.topbar__url{left:163px;top:8px;font-size:11px;color:#444}
.topbar__social{right:167px;top:8px;display:flex;gap:14px}
.topbar__social span{width:16px;height:16px;border-radius:50%;background:var(--navy)}
.topbar__social span:first-child{background:var(--green)}

.header{left:0;top:31px;width:1200px;height:71px}
.header__title{left:160px;top:18px;font-family:"Roboto Condensed",Arial,sans-serif;font-size:28px;color:var(--green)}
.header__links{right:161px;top:25px;display:flex;align-items:center;gap:18px;font-size:13.5px;font-weight:500;color:var(--navy)}
.header__links .contact{display:flex;align-items:center;gap:9px}

.nav{left:0;top:102px;width:1200px;height:48px;background:var(--navy)}
.nav ul{position:absolute;left:166px;top:0;display:flex;list-style:none;height:48px}
.nav li{padding:0 8px;line-height:48px;font-size:14px;font-weight:500;color:var(--white);letter-spacing:.2px}
.nav li.is-active{background:var(--green);color:var(--navy)}

.hero{left:0;top:150px;width:1200px;height:166px;background:#bac4cf}
.hero__visual{left:522px;top:0;width:678px;height:166px;background:linear-gradient(90deg,#b6c0cb 0%,#a7b2bf 30%,#d3dae2 70%,#e4e9ee 100%)}
.hero__dash{left:160px;top:49px;width:27px;height:2px;background:var(--navy)}
.hero__title{left:158px;top:56px;font-size:48px;font-weight:700;color:var(--navy)}

.strip{left:0;top:316px;width:1200px;height:85px;background:var(--grey-soft)}
.strip__heading{left:178px;top:25px;font-size:27px;font-weight:700;color:var(--navy)}

.intro__heading{left:0;top:450px;width:1200px;text-align:center;font-size:30px;font-weight:500;color:var(--navy)}
.intro__text{left:250px;top:540px;width:700px;text-align:center;font-size:17px;font-weight:300;line-height:27px;color:var(--text-muted)}

.contact-card{left:397px;top:639px;width:406px;height:236px;background:var(--grey-soft)}
.contact-card__bar{left:2px;top:55px;width:7px;height:119px;background:var(--green)}
.contact-card__name{left:92px;top:56px;font-size:20px;font-weight:700;color:var(--navy)}
.contact-card__phones{left:92px;top:108px;font-size:20px;font-weight:300;line-height:27px;color:#8a8a8a}

.cta{left:0;top:950px;width:1200px;height:169px;background:linear-gradient(110deg,var(--navy) 0%,var(--navy-2) 35%,#2d3e5b 55%,var(--navy-2) 80%,var(--navy) 100%)}
.cta__heading{left:158px;top:62px;font-size:42px;font-weight:500;color:var(--green)}
.cta__phone{left:713px;top:70px;display:flex;align-items:center;gap:17px;font-size:33px;font-weight:300;color:var(--white)}

.footer{left:0;top:1119px;width:1200px;height:49px;background:var(--green);text-align:center;line-height:49px;font-size:12px;color:#1f2b3d}
</style>
</head>
<body>

<div class="abs topbar">
  <div class="abs topbar__url">www.projektor-verleih-region-wendlar.de</div>
  <div class="abs topbar__social"><span></span><span></span><span></span><span></span></div>
</div>

<header class="abs header">
  <div class="abs header__title">Beamer Vermietung zu Günstigen Konditionen</div>
  <nav class="abs header__links">
    <span class="contact">
      <svg width="20" height="14" viewBox="0 0 20 14"><rect x="1" y="1" width="18" height="12" fill="none" stroke="#2c3c57" stroke-width="1.2"/><path d="M1 1 L10 8 L19 1" fill="none" stroke="#2c3c57" stroke-width="1.2"/></svg>
      Kontakt / Anreise
    </span>
    <span>Impressum</span>
  </nav>
</header>

<nav class="abs nav">
  <ul>
    <li>Startseite</li>
    <li>Beamer mieten</li>
    <li>HD-Beamer mieten</li>
    <li>Full HD-Beamer</li>
    <li>Leinwand mieten</li>
    <li class="is-active">Reservierung</li>
    <li>Preisliste</li>
    <li>Datenschutz</li>
  </ul>
</nav>

<section class="abs hero">
  <div class="abs hero__visual" role="img" aria-label="Foto einer Stadtsilhouette mit Kommunikationssymbolen: Telefon, At-Zeichen, Brief und Mobiltelefon"></div>
  <div class="abs hero__dash"></div>
  <h1 class="abs hero__title">Reservieren</h1>
</section>

<section class="abs strip">
  <svg class="abs" style="left:0;top:0" width="1200" height="85">
    <circle cx="127" cy="52" r="12" fill="#97c24b"/>
    <circle cx="154" cy="33" r="5" fill="#2c3c57"/>
    <circle cx="943" cy="45" r="30" fill="#97c24b"/>
  </svg>
  <h2 class="abs strip__heading">Reservieren oder Buchen</h2>
</section>

<h2 class="abs intro__heading">Sie haben Interesse an unserer Beamer Vermietung?</h2>
<p class="abs intro__text">Dann rufen Sie uns einfach unter einer der unten stehenden Telefonnummern an und fragen Sie nach der Verfügbarkeit des gewünschten Beamers:</p>

<div class="abs contact-card">
  <div class="abs contact-card__bar"></div>
  <div class="abs contact-card__name">Hollmer Steinkamp GbR</div>
  <div class="abs contact-card__phones">Festnetz: 02791/ 483205<br>Mobil: 0157 / 2846193</div>
</div>

<section class="abs cta">
  <h2 class="abs cta__heading">Reservieren oder Buchen</h2>
  <div class="abs cta__phone">
    <svg width="33" height="24" viewBox="0 0 33 24"><path d="M2 8 Q16.5 -2 31 8 L28 12 L22 10 L22 7 Q16.5 5 11 7 L11 10 L5 12 Z" fill="#97c24b"/><path d="M8 12 L25 12 L29 23 L4 23 Z" fill="#97c24b"/><circle cx="16.5" cy="17" r="3.5" fill="#2c3c57"/></svg>
    <span>Tel: 0157 / 6081437</span>
  </div>
</section>

<footer class="abs footer">Copyright © 2020.&nbsp; Projektor-verleih-region-wendlar.de</footer>

</body>
</html>
```